Bright Path Mission- a non profit locin TZ , east Africa. Needing to attract donors.

A flyer for donors /potential partners. showing what their giving has accomplished this year. An Encouraging way to say thank you at the same time informing the partner of the amazing things God is doing with their generous, faithful giving. We will need to print/email. Thank you for considering this project. Your efforts help in educating and feeding 225 street children, providing a safe haven and trade school for hundreds of women and abused teenagers, medical ship on the longest lake in the world going into unreached people groups, a Bible College Training up pastors to plant churches all over TZ, Congo, Burundi and beyond, youth and children’s kids clubs and youth camps. These are the main areas of bright path mission. Bible college, primary school, trade schools, youth camps/kids clubs. We need help in making sure readers will be drawn to seeing/reading more which leads to donations without overwhelming with too much info. HELP! I can tell you about Jesus I have even authored 7 books, but making s flyer that makes sense it out of my wheelhouse. Again, thank you.
Updates

I do not want longer I need quicker and paid for a 3 day quote. All pictures and logo are on our website. I have tried to send pictures but they won’t send. Please look at. Www.brightpathmissiontz.org

Target Market(s)

Professional adults, large companies, donors

Industry/Entity Type

Non profit missionary Bright Path Mission in Tanzania, Congo, USA and soon to be Canada.

Requirements
Must have
• Color professional pictures, feel good, exciting want to be apart of what God is doing
Nice to have
• Glossy trifold
Should not have
• Fly in the face, guilt feeling, animals in Africa

```html
<!DOCTYPE html>
<html lang="en">
<head>
<meta charset="utf-8">
<title>Bright Path Mission – Thank You Trifold</title>
<link href="https://fonts.googleapis.com/css2?family=Exo+2:ital,wght@0,400;0,600;0,700;0,800;1,700&family=Open+Sans:wght@400;600;700&display=swap" rel="stylesheet">
<style>
  :root{
    --charcoal:#3b3b3b;
    --charcoal-deep:#2c2c2c;
    --olive:#c4cc8c;
    --olive-soft:#d2d8a6;
    --olive-deep:#8f9a52;
    --paper:#f4f4f1;
    --ink:#2d2d2d;
    --backdrop:#e7e6e1;
  }
  *{box-sizing:border-box;margin:0;padding:0}
  html,body{width:1200px;height:675px;overflow:hidden;background:var(--backdrop)}
  body{position:relative;font-family:"Open Sans",Arial,sans-serif;color:var(--ink)}
  .sheet{position:absolute;top:108px;width:576px;height:460px;display:flex;box-shadow:0 6px 18px rgba(0,0,0,.18)}
  .sheet--outside{left:16px}
  .sheet--inside{left:608px}
  .panel{position:relative;width:192px;height:460px;overflow:hidden}
  .panel + .panel{border-left:1px solid rgba(0,0,0,.08)}
  .photo{display:block}
  .display{font-family:"Exo 2",Arial,sans-serif}
  .url{font-family:"Exo 2",Arial,sans-serif;font-weight:700;font-size:8px;text-align:center;letter-spacing:.2px}

  /* outside: service list panel */
  .panel--services{background:var(--paper);padding:22px 16px}
  .service{display:flex;gap:8px;margin-bottom:26px}
  .service__icon{flex:0 0 26px}
  .service h3{font-family:"Exo 2",Arial,sans-serif;font-weight:700;font-size:12px;line-height:1.05;margin-bottom:5px}
  .service p{font-size:6px;line-height:1.45}

  /* outside: mission panel */
  .panel--mission{background:var(--olive)}
  .panel--mission .photo{position:absolute;inset:0;background:linear-gradient(180deg,#b7bf7e 0%,#c4cc8c 45%,#a9ae7a 100%)}
  .mission__body{position:relative;padding:70px 16px 0;text-align:center}
  .mission__lead{font-family:"Exo 2",Arial,sans-serif;font-weight:800;font-size:17px;line-height:1.05;text-transform:uppercase;color:var(--ink)}
  .mission__sub{font-family:"Exo 2",Arial,sans-serif;font-weight:700;font-size:12px;line-height:1.15;margin-top:4px}
  .mission__ref{font-family:"Exo 2",Arial,sans-serif;font-weight:700;font-size:12px;margin-top:14px}
  .contact{position:absolute;left:16px;right:16px;bottom:34px;text-align:center;font-size:7px;line-height:1.5;font-weight:600}
  .contact__name{font-family:"Exo 2",Arial,sans-serif;font-weight:700;font-size:12px;margin-bottom:6px}

  /* outside: cover */
  .panel--cover{background:var(--charcoal);color:#fff}
  .cover__brand{text-align:center;padding-top:18px}
  .cover__brand .small{font-family:"Exo 2",Arial,sans-serif;font-size:14px;letter-spacing:1px;color:var(--olive-soft)}
  .cover__brand .big{font-family:"Exo 2",Arial,sans-serif;font-weight:800;font-size:27px;line-height:.95;color:var(--olive)}
  .cover__brand .verse{font-size:5.5px;font-style:italic;margin-top:3px}
  .cover__brand .country{font-family:"Exo 2",Arial,sans-serif;font-weight:700;font-size:7px;letter-spacing:1px}
  .cover__thanks{padding:14px 12px 0}
  .cover__thanks .t1{font-family:"Exo 2",Arial,sans-serif;font-weight:800;font-size:25px;line-height:1;color:var(--olive)}
  .cover__thanks .t2{font-family:"Exo 2",Arial,sans-serif;font-weight:700;font-size:10px;line-height:1.1;text-transform:uppercase}
  .panel--cover .photo{position:absolute;left:0;right:0;top:178px;height:150px;background:linear-gradient(160deg,#4e5058 0%,#6d6a66 50%,#3a3d44 100%);border-top:3px solid var(--olive);border-bottom:3px solid var(--olive)}
  .cover__text{position:absolute;top:338px;left:14px;right:14px;text-align:center;font-size:6.4px;line-height:1.5}
  .pill{position:absolute;left:22px;right:22px;bottom:14px;height:20px;border-radius:10px;background:var(--olive);color:var(--ink);display:flex;align-items:center;justify-content:center}

  /* inside panels */
  .inside-top{position:absolute;top:0;left:0;right:0;height:72px;background:linear-gradient(180deg,#2a2a2a,#4a4a4a)}
  .inside-title{position:absolute;top:34px;left:14px;font-family:"Exo 2",Arial,sans-serif;font-weight:700;font-size:17px;color:var(--olive)}
  .inside-body{position:absolute;top:72px;left:0;right:0;height:240px;padding:10px 12px}
  .panel--about .inside-body{background:var(--olive)}
  .panel--serve .inside-body{background:#fff}
  .inside-body p{font-size:5.6px;line-height:1.5;margin-bottom:5px;text-align:justify}
  .tag{display:inline-block;background:var(--charcoal);color:#fff;font-family:"Exo 2",Arial,sans-serif;font-weight:700;font-style:italic;font-size:8px;padding:2px 10px 2px 6px;margin:2px 0 5px -12px;text-transform:uppercase;clip-path:polygon(0 0,100% 0,92% 100%,0 100%)}
  .panel--serve:last-child .tag{background:none;color:var(--ink);margin-left:0;padding-left:0}
  .inside-bottom{position:absolute;top:312px;left:0;right:0;bottom:0;background:var(--charcoal)}
  .inside-bottom .photo{position:absolute;top:12px;left:12px;right:12px;height:92px;border:2px solid #eee}
  .inside-bottom .url{position:absolute;left:0;right:0;bottom:14px;color:var(--olive)}
</style>
</head>
<body>

<section class="sheet sheet--outside" aria-label="Trifold outside">
  <article class="panel panel--services">
    <div class="service">
      <svg class="service__icon" viewBox="0 0 26 26" width="26" height="26" aria-hidden="true"><circle cx="13" cy="13" r="10" fill="none" stroke="#a58a4f" stroke-width="2"/><path d="M13 7v12M7 13h12" stroke="#a58a4f" stroke-width="2"/></svg>
      <div><h3>How we<br>SERVE</h3><p>Our mission is to raise up a generation of young people who are firmly grounded in their relationship with Jesus Christ.</p></div>
    </div>
    <div class="service">
      <svg class="service__icon" viewBox="0 0 26 26" width="26" height="26" aria-hidden="true"><path d="M13 23 3 12a5.5 5.5 0 0 1 10-6 5.5 5.5 0 0 1 10 6Z" fill="#c0202a"/></svg>
      <div><h3>Partner<br>WITH US</h3><p>By partnering with Bright Path Mission you are never simply a sponsor or donor. You are changing lives in East Africa.</p></div>
    </div>
    <div class="service">
      <svg class="service__icon" viewBox="0 0 26 26" width="26" height="26" aria-hidden="true"><rect x="5" y="2" width="16" height="22" rx="1" fill="#3f8fd0"/><rect x="7" y="2" width="2" height="22" fill="#2c6ea6"/></svg>
      <div><h3>Are you a<br>BIBLE<br>TEACHER?</h3><p>We depend on visiting pastors and Bible teachers. Come make an impact on students who hunger to learn God's word.</p></div>
    </div>
  </article>

  <article class="panel panel--mission">
    <div class="photo" role="img" aria-label="Faded photo of a smiling child in warm green tones"></div>
    <div class="mission__body">
      <p class="mission__lead">To bring<br>hope to the<br>nations</p>
      <p class="mission__sub">through the knowledge of Jesus Christ and the Word of God.</p>
      <p class="mission__ref">Matt. 12:21</p>
    </div>
    <div class="contact">
      <p class="contact__name">Bright Path Mission</p>
      <p>PO Box 4410<br>Lakeside, CA 95000</p>
      <p>info@brightpathmissiontz.org</p>
      <p>www.brightpathmissiontz.org</p>
    </div>
  </article>

  <article class="panel panel--cover">
    <header class="cover__brand">
      <p class="small">BRIGHT PATH</p>
      <p class="big">MISSION</p>
      <p class="verse">"In His name the nations will put their hope." Mt. 12:21</p>
      <p class="country">TANZANIA</p>
    </header>
    <div class="cover__thanks">
      <p class="t1">THANK YOU!</p>
      <p class="t2">For considering this<br>project</p>
    </div>
    <div class="photo" role="img" aria-label="Photo of schoolchildren in checked uniforms praying"></div>
    <p class="cover__text">Your efforts help in educating and feeding 225 street children, providing a safe haven and trade school for hundreds of women and abused teenagers, medical ship on the longest lake in the world going into unreached people groups, a Bible College training up pastors to plant churches all over TZ, Congo, Burundi and beyond, youth and children's kids clubs and youth camps.</p>
    <p class="pill url">www.brightpathmissiontz.org</p>
  </article>
</section>

<section class="sheet sheet--inside" aria-label="Trifold inside">
  <article class="panel panel--about">
    <div class="inside-top photo" role="img" aria-label="Dark photo of children gathered together"></div>
    <h2 class="inside-title">About Us</h2>
    <div class="inside-body">
      <p>Bright Path Mission has its headquarters in Kigoma, Tanzania, on the shores of Lake Tanganyika, the longest lake in the world. From this port town we reach families in Tanzania, Congo, Burundi and beyond.</p>
      <p>Founded in 2007 by David and Ruth Maren, the ministry now employs more than forty local staff, all working to raise up believers who will carry the good news to every village around the lake.</p>
      <p>Through Christ, the hope that is found in Him is beginning to reach this region and its neighbors.</p>
    </div>
    <div class="inside-bottom">
      <div class="photo" role="img" aria-label="Photo of students learning at computers with headphones" style="background:linear-gradient(150deg,#8a7d70,#c9bfae 55%,#5e5650)"></div>
      <p class="url">www.brightpathmissiontz.org</p>
    </div>
  </article>

  <article class="panel panel--serve">
    <div class="inside-top photo" role="img" aria-label="Dark photo of a worship gathering"></div>
    <h2 class="inside-title">How We Serve</h2>
    <div class="inside-body">
      <span class="tag">Education</span>
      <p>Our vision is to raise up a generation of godly influencers grounded in their relationship with Jesus Christ. We started with a preschool, which has grown into a primary school with over 200 students.</p>
      <p>Our Bible College trains pastors to study and teach the Word, then go out to plant churches.</p>
      <span class="tag">Village Outreaches</span>
      <p>Our outreaches bring help and hope to remote villages along the lake, with medical care, seminars and evening gatherings. We gladly host teams from North America.</p>
    </div>
    <div class="inside-bottom">
      <div class="photo" role="img" aria-label="Photo of women sewing at a vocational training class" style="background:linear-gradient(150deg,#7a5a4a,#b3927a 50%,#4f4a48)"></div>
      <p class="url">www.brightpathmissiontz.org</p>
    </div>
  </article>

  <article class="panel panel--serve">
    <div class="inside-top photo" role="img" aria-label="Dark photo of youth with raised hands"></div>
    <h2 class="inside-title">How We Serve</h2>
    <div class="inside-body">
      <span class="tag">Kid's Clubs</span>
      <p>Kid's Clubs began as an outreach to children living on the streets. Twice a week they receive food, play games and hear the Word of God. The ministry has grown to over 1000 kids in 14 locations.</p>
      <p>We also hold summer camps each year for youth to refresh and train new leaders.</p>
      <span class="tag">Micro-Businesses</span>
      <p>Jobs are hard to come by. Through our Vocational Training Center, men and women learn sewing, welding, baking and carpentry, and small loans help grads start their own business.</p>
    </div>
    <div class="inside-bottom">
      <div class="photo" role="img" aria-label="Photo of smiling children in a classroom" style="background:linear-gradient(150deg,#5b6a7a,#a8b0a8 50%,#3e4650)"></div>
      <p class="url">www.brightpathmissiontz.org</p>
    </div>
  </article>
</section>

</body>
</html>
```